Comic book online retailer needs web design

Need a website designed for us to upload via FTP.
Our business is selling comic books and super hero related collectibles through Tradoo exclusively. Our logo has been uploaded. Our slogan is "Big Kids Helping Little Kids" because we donate a portion of our profits to children's charities.
We are looking for a clean, modern, "cool" design that represents the points given above. The site should be fun but easy on the eyes. Navigation should intuitive and easy to find. I would say we are looking for a design that would look and feel at home with Quenby products websites. it should look like a comic book / super hero business website and not a technology product website.
Target Market(s)
Our target demographic is 15 to 35 year old males.
Industry/Entity Type
Business
Coding
Coded - Design and coding required
Number of Pages Required
2 page
Font styles to use
Other font styles liked:
- Comicpro or font similar to our logo
Requirements
Must have
- Tradoo "button" or image that takes them directly to our Tradoo items for sale page here... http://www.tradoo.example/sch/vantelpanels/m.html?_nkw=&_armrs=1&_from=&_ipg=25&_trksid=p3692
- A widget that cycles through our items listed for sale. Prefer something that slides through the items, perhaps showing 4 to 6 items at a time. Tradoo user ID is vantelpanels
- Our slogan - “Big Kids Helping Little Kids”.
- Our mission statement - "To support children’s charities with a portion of our profits. We believe happy kids become happy adults."
- Contact info - email = martin@vantelpanels.example, phone number 555-210-3389, mail = PO Box 482 Larkfield Valley 17099
Nice to have
- separate page for charities supported with links to their information page. We currently support the Young Ones Hope Circle in Hershey (http://www.larkfieldyohc.example/index.cfm?fuseaction=cms.home) and the Larkfield Valley Children's Hospital(http://www.larkfieldvalley.example/web/childrens)
- clicking on email in contacts should open a window to generate email message
Should not have
- too childish or cartoony
- too bright or too busy
- blatant use or copies of trademarked characters (like Skyvaultor, Nightwren, ect)

```html
<!DOCTYPE html>
<html lang="en">
<head>
<meta charset="utf-8">
<title>Vantel Panels &amp; Collectibles</title>
<link rel="stylesheet" href="https://fonts.googleapis.com/css2?family=Montserrat:wght@300;400;700&family=Open+Sans:wght@400;600;700;800&display=swap">
<style>
:root{
  --blue:#6cc9df;
  --yellow:#efbf48;
  --orange:#ee7b54;
  --green:#6fc592;
  --red:#e7686b;
  --purple:#b78dd0;
  --action:#4d86ee;
  --ink:#3b3c3f;
  --muted:#9a9ca0;
  --footer:#4a4b4e;
  --footer-deep:#3a3b3d;
  --topbar:#3f4043;
  --white:#ffffff;
}
*{box-sizing:border-box;margin:0;padding:0}
html,body{width:1200px;height:3310px;overflow:hidden}
body{position:relative;background:var(--white);font-family:"Open Sans",Arial,sans-serif;color:var(--ink)}
.abs{position:absolute}

/* hero */
.hero-photo{left:0;top:0;width:1200px;height:731px;
  background:linear-gradient(100deg,#cfd6d8 0%,#a9c3c7 22%,#5f8a8e 45%,#8fb0b5 62%,#d7dcdc 85%,#e9ecec 100%)}
.hero-arrow{width:48px;height:48px;border-radius:50%;background:rgba(255,255,255,.35);top:404px}
.hero-arrow svg{display:block;margin:14px auto}
.hero-line{font-family:"Open Sans",sans-serif;font-weight:800;font-size:30px;letter-spacing:1px;text-align:center;line-height:64px}
.hero-line.dark{left:635px;top:350px;width:391px;height:64px;background:rgba(45,46,48,.82);color:var(--white)}
.hero-line.light{left:704px;top:422px;width:322px;height:69px;background:rgba(255,255,255,.88);color:var(--ink);line-height:69px}

/* top bar + header */
.topbar{left:138px;top:0;width:924px;height:33px;background:var(--topbar);color:#d9d9d9;font-size:11px;display:flex;align-items:center;padding:0 40px}
.topbar span{display:flex;align-items:center;gap:8px;margin-right:46px}
.topbar .social{margin-left:auto;display:flex;gap:18px;margin-right:0}
.topbar .social i{display:block;width:10px;height:10px;border-radius:2px;background:#cfcfcf}
.header{left:138px;top:33px;width:924px;height:150px;background:rgba(255,255,255,.97);display:flex;align-items:center;padding:0 28px}
.brand{display:flex;align-items:center;gap:12px;width:300px}
.brand-dot{width:38px;height:38px;border-radius:50%;background:var(--red)}
.brand-name{font-family:"Open Sans",sans-serif;font-weight:800;font-size:22px;color:var(--ink);line-height:1.05}
.nav{display:flex;align-items:center;margin-left:30px;font-family:"Montserrat",sans-serif;font-size:12px;letter-spacing:1.5px;color:#8a8c90}
.nav a{color:inherit;text-decoration:none}
.nav .dot{width:5px;height:5px;border-radius:50%;margin:0 34px}
.header-btn{width:36px;height:36px;background:var(--action);display:flex;align-items:center;justify-content:center;margin-left:14px}
.header-btn.first{margin-left:44px}

/* category tabs */
.tabs{left:138px;top:662px;width:924px;height:69px;display:flex}
.tab{flex:1;color:var(--white);font-family:"Montserrat",sans-serif;font-size:14px;letter-spacing:1.5px;display:flex;align-items:center;justify-content:center;text-transform:uppercase}

/* welcome */
.welcome{left:0;top:790px;width:1200px;text-align:center}
.welcome-kicker{font-family:"Montserrat",sans-serif;font-weight:300;font-size:22px;letter-spacing:3px;color:#8d8f93}
.welcome-title{font-family:"Montserrat",sans-serif;font-weight:700;font-size:24px;letter-spacing:3px;color:var(--ink);margin-top:8px}
.welcome-rule{width:70px;height:3px;background:var(--green);margin:20px auto 0}
.welcome-slogan{font-size:15px;color:#a8aaae;margin-top:22px}

/* tiles */
.tile{width:298px}
.tile-photo{position:relative}
.tile-zoom{position:absolute;left:28px;top:26px;width:44px;height:44px;border-radius:50%;display:flex;align-items:center;justify-content:center;opacity:.92}
.tile-body{color:var(--white);padding:22px 22px 0;position:relative}
.tile-title{font-weight:700;font-size:14px}
.tile-rule{width:34px;height:2px;background:rgba(255,255,255,.7);margin:12px 0 10px}
.tile-text{font-size:10.5px;line-height:1.55;opacity:.92}
.tile-more{display:flex;align-items:center;gap:10px;font-family:"Montserrat",sans-serif;font-size:10px;font-weight:700;letter-spacing:1px;margin-top:14px}
.blue{background:var(--blue)}.yellow{background:var(--yellow)}.orange{background:var(--orange)}
.green{background:var(--green)}.red{background:var(--red)}.purple{background:var(--purple)}

/* mission band */
.mission{left:0;top:2006px;width:1200px;height:270px;
  background:linear-gradient(180deg,rgba(40,40,40,.25),rgba(40,40,40,.45)),linear-gradient(90deg,#d9a883 0%,#c6b77c 30%,#9fbf72 55%,#d5a07b 80%,#c98a6c 100%)}
.mission-text{left:0;top:2100px;width:1200px;text-align:center;color:var(--white)}
.mission-lead{font-family:"Montserrat",sans-serif;font-size:17px;letter-spacing:1.5px}
.mission-main{font-family:"Montserrat",sans-serif;font-size:24px;letter-spacing:2px;margin-top:10px}
.btn{background:var(--action);color:var(--white);font-family:"Montserrat",sans-serif;font-size:12px;letter-spacing:1.5px;display:flex;align-items:center;justify-content:center}
.mission-btn{left:477px;top:2207px;width:246px;height:60px}

/* products */
.product{width:450px;height:186px;display:flex;background:#f3f3f3}
.product-cover{width:152px;display:flex;align-items:center;justify-content:center;background:var(--white)}
.product-cover div{width:54px;height:74px}
.product-body{flex:1;color:var(--white);padding:22px 24px;position:relative}
.product-body .tile-text{width:200px}
.product-actions{position:absolute;right:20px;top:18px;display:flex;flex-direction:column;gap:12px}
.product-actions span{width:36px;height:36px;border-radius:50%;background:rgba(255,255,255,.25);display:flex;align-items:center;justify-content:center}
.more-btn{left:469px;top:2800px;width:262px;height:68px;font-size:13px}

/* footer */
.footer{left:0;top:2911px;width:1200px;height:345px;background:var(--footer);border-top:4px solid var(--orange)}
.footer-h{font-family:"Montserrat",sans-serif;font-size:17px;letter-spacing:1px;color:var(--white)}
.field{font-size:9px;letter-spacing:1px;color:#b8b9bc;border-bottom:1px solid #6d6e71;padding-bottom:10px}
.send{left:450px;top:3165px;width:130px;height:36px;font-size:11px}
.gallery{left:629px;top:3026px;width:218px;display:grid;grid-template-columns:repeat(3,70px);gap:4px}
.gallery div{height:32px}
.detail{display:flex;align-items:center;gap:16px;font-size:11px;color:#d5d6d8;margin-bottom:22px;white-space:nowrap}
.bottom{left:0;top:3256px;width:1200px;height:54px;background:var(--footer-deep);display:flex;align-items:center;padding:0 138px;font-size:11px;color:#c9cacc}
.bottom .social{margin-left:auto;display:flex;gap:12px}
.bottom .social i{display:block;width:24px;height:24px}
</style>
</head>
<body>

<div class="abs hero-photo" role="img" aria-label="Photo of a smiling mother and young son reading a picture book in a bookshop aisle"></div>
<div class="abs hero-arrow" style="left:64px"><svg width="20" height="20" viewBox="0 0 20 20"><path d="M13 3 6 10l7 7" stroke="#fff" stroke-width="2.5" fill="none"/></svg></div>
<div class="abs hero-arrow" style="left:1088px"><svg width="20" height="20" viewBox="0 0 20 20"><path d="M7 3l7 7-7 7" stroke="#fff" stroke-width="2.5" fill="none"/></svg></div>
<div class="abs hero-line dark">BIG KIDS HELPING</div>
<div class="abs hero-line light">LITTLE KIDS !</div>

<div class="abs topbar">
  <span><svg width="12" height="9" viewBox="0 0 12 9"><rect x=".5" y=".5" width="11" height="8" fill="none" stroke="#ccc"/><path d="M.5.5 6 5l5.5-4.5" fill="none" stroke="#ccc"/></svg>martin@vantelpanels.example</span>
  <span><svg width="10" height="10" viewBox="0 0 10 10"><path d="M2 0 4 3 3 4.5Q4.5 7 6 7L7 6l3 2-1.5 2Q1 9 0 1.5Z" fill="#ccc"/></svg>555-210-3389</span>
  <span><svg width="8" height="11" viewBox="0 0 8 11"><path d="M4 11S0 6 0 4a4 4 0 0 1 8 0c0 2-4 7-4 7Z" fill="#ccc"/></svg>PO Box 482 Larkfield Valley 17099</span>
  <span class="social"><i></i><i></i></span>
</div>

<header class="abs header">
  <div class="brand"><div class="brand-dot"></div><div class="brand-name">Vantel<br>Panels</div></div>
  <nav class="nav">
    <a href="#">HOME</a><span class="dot" style="background:var(--yellow)"></span>
    <a href="#">ABOUT</a><span class="dot" style="background:var(--orange)"></span>
    <a href="#">COMIC</a><span class="dot" style="background:var(--green)"></span>
    <a href="#">STORE</a><span class="dot" style="background:var(--red)"></span>
    <a href="#">CONTACT</a>
  </nav>
  <div class="header-btn first"><svg width="16" height="16" viewBox="0 0 16 16"><circle cx="6.5" cy="6.5" r="5" fill="none" stroke="#fff" stroke-width="2"/><path d="m10 10 5 5" stroke="#fff" stroke-width="2"/></svg></div>
  <div class="header-btn"><svg width="18" height="16" viewBox="0 0 18 16"><path d="M0 1h3l2 9h10l2-7H4.5" fill="none" stroke="#fff" stroke-width="1.8"/><circle cx="6" cy="14" r="1.5" fill="#fff"/><circle cx="14" cy="14" r="1.5" fill="#fff"/></svg></div>
</header>

<div class="abs tabs">
  <div class="tab blue">Comics</div>
  <div class="tab yellow">Super-Heros</div>
  <div class="tab orange">Store</div>
  <div class="tab green">Tradoo</div>
</div>

<section class="abs welcome">
  <div class="welcome-kicker">HELLO &amp; WELCOME TO THE</div>
  <div class="welcome-title">VANTEL PANELS &amp; COLLECTIBLES</div>
  <div class="welcome-rule"></div>
  <div class="welcome-slogan">Big Kids Helping Little Kids</div>
</section>

<!-- column one -->
<article class="abs tile" style="left:138px;top:966px">
  <div class="tile-photo" style="height:207px;background:linear-gradient(135deg,#efe3d6,#d8b99c 60%,#b98f74)" role="img" aria-label="Photo of a mother reading a book to her baby"><span class="tile-zoom orange"><svg width="14" height="14" viewBox="0 0 16 16"><circle cx="6.5" cy="6.5" r="5" fill="none" stroke="#fff" stroke-width="2"/><path d="m10 10 5 5" stroke="#fff" stroke-width="2"/></svg></span></div>
  <div class="tile-body blue" style="height:157px"><div class="tile-title">Big Kids Helping Little Kids !</div><div class="tile-rule"></div><div class="tile-text">Every comic sold helps a child smile. We give part of each sale to local kids.</div><div class="tile-more"><svg width="14" height="10" viewBox="0 0 14 10"><path d="M0 1h14M0 5h14M0 9h14" stroke="#fff"/></svg>READ MORE</div></div>
</article>
<article class="abs tile" style="left:138px;top:1344px">
  <div class="tile-photo" style="height:187px;background:linear-gradient(180deg,#eef4f7,#b9d3a2 70%,#8db06e)" role="img" aria-label="Photo of children in capes standing on a lawn"></div>
  <div class="tile-body green" style="height:157px"><div class="tile-title">Big Kids Helping Little Kids !</div><div class="tile-rule"></div><div class="tile-text">Every comic sold helps a child smile. We give part of each sale to local kids.</div><div class="tile-more"><svg width="14" height="10" viewBox="0 0 14 10"><path d="M0 1h14M0 5h14M0 9h14" stroke="#fff"/></svg>READ MORE</div></div>
</article>
<article class="abs tile" style="left:138px;top:1711px">
  <div class="tile-photo" style="height:110px;background:linear-gradient(135deg,#f6efe8,#e7d3c3 60%,#cfb09a)" role="img" aria-label="Photo of a mother and baby reading together"><span class="tile-zoom orange"><svg width="14" height="14" viewBox="0 0 16 16"><circle cx="6.5" cy="6.5" r="5" fill="none" stroke="#fff" stroke-width="2"/><path d="m10 10 5 5" stroke="#fff" stroke-width="2"/></svg></span></div>
  <div class="tile-body orange" style="height:124px"><div class="tile-title">Big Kids Helping Little Kids !</div><div class="tile-rule"></div><div class="tile-more"><svg width="14" height="10" viewBox="0 0 14 10"><path d="M0 1h14M0 5h14M0 9h14" stroke="#fff"/></svg>READ MORE</div></div>
</article>

<!-- column two -->
<article class="abs tile" style="left:450px;top:971px">
  <div class="tile-body green" style="height:155px"><div class="tile-title">Big Kids Helping Little Kids !</div><div class="tile-rule"></div><div class="tile-text">Every comic sold helps a child smile. We give part of each sale to local kids.</div><div class="tile-more"><svg width="14" height="10" viewBox="0 0 14 10"><path d="M0 1h14M0 5h14M0 9h14" stroke="#fff"/></svg>READ MORE</div></div>
</article>
<article class="abs tile" style="left:450px;top:1150px">
  <div class="tile-photo" style="height:202px;background:linear-gradient(135deg,#d9e6ee,#8fb6d6 50%,#e7c28f)" role="img" aria-label="Photo of a grandmother reading to two children"></div>
  <div class="tile-body orange" style="height:48px;padding-top:15px"><div class="tile-title">Big Kids Helping Little Kids !</div></div>
</article>
<article class="abs tile" style="left:450px;top:1407px">
  <div class="tile-photo" style="height:193px;background:linear-gradient(180deg,#e9f0f4,#c9dbe3 55%,#d8c7a4)" role="img" aria-label="Photo of kids in superhero costumes on a beach"><span class="tile-zoom yellow"><svg width="14" height="14" viewBox="0 0 16 16"><circle cx="6.5" cy="6.5" r="5" fill="none" stroke="#fff" stroke-width="2"/><path d="m10 10 5 5" stroke="#fff" stroke-width="2"/></svg></span></div>
  <div class="tile-body yellow" style="height:160px"><div class="tile-title">Big Kids Helping Little Kids !</div><div class="tile-rule"></div><div class="tile-text">Every comic sold helps a child smile. We give part of each sale to local kids.</div><div class="tile-more"><svg width="14" height="10" viewBox="0 0 14 10"><path d="M0 1h14M0 5h14M0 9h14" stroke="#fff"/></svg>READ MORE</div></div>
</article>
<article class="abs tile" style="left:450px;top:1780px">
  <div class="tile-body red" style="height:165px"><div class="tile-title">Big Kids Helping Little Kids !</div><div class="tile-rule"></div><div class="tile-text">Every comic sold helps a child smile. We give part of each sale to local kids.</div><div class="tile-more"><svg width="14" height="10" viewBox="0 0 14 10"><path d="M0 1h14M0 5h14M0 9h14" stroke="#fff"/></svg>READ MORE</div></div>
</article>

<!-- column three -->
<article class="abs tile" style="left:764px;top:971px">
  <div class="tile-photo" style="height:188px;background:linear-gradient(180deg,#7fb3df,#b8d6ee 60%,#e9eef2)" role="img" aria-label="Photo of a boy in a superhero cape against a blue sky"><span class="tile-zoom purple"><svg width="14" height="14" viewBox="0 0 16 16"><circle cx="6.5" cy="6.5" r="5" fill="none" stroke="#fff" stroke-width="2"/><path d="m10 10 5 5" stroke="#fff" stroke-width="2"/></svg></span></div>
  <div class="tile-body purple" style="height:55px;padding-top:19px"><div class="tile-title">Big Kids Helping Little Kids !</div></div>
</article>
<article class="abs tile" style="left:764px;top:1233px">
  <div class="tile-photo" style="height:197px;background:linear-gradient(135deg,#eceeee,#c7cccc 55%,#a9a6a3)" role="img" aria-label="Photo of a father and son looking at a phone on the sofa"><span class="tile-zoom red"><svg width="14" height="14" viewBox="0 0 16 16"><circle cx="6.5" cy="6.5" r="5" fill="none" stroke="#fff" stroke-width="2"/><path d="m10 10 5 5" stroke="#fff" stroke-width="2"/></svg></span></div>
  <div class="tile-body red" style="height:148px"><div class="tile-title">Big Kids Helping Little Kids !</div><div class="tile-rule"></div><div class="tile-text">Every comic sold helps a child smile. We give part of each sale to local kids.</div><div class="tile-more"><svg width="14" height="10" viewBox="0 0 14 10"><path d="M0 1h14M0 5h14M0 9h14" stroke="#fff"/></svg>READ MORE</div></div>
</article>
<article class="abs tile" style="left:764px;top:1600px">
  <div class="tile-photo" style="height:180px;background:linear-gradient(135deg,#f3ede6,#dcc4b4 55%,#c49c86)" role="img" aria-label="Photo of a mother and daughter reading on a bed"><span class="tile-zoom blue"><svg width="14" height="14" viewBox="0 0 16 16"><circle cx="6.5" cy="6.5" r="5" fill="none" stroke="#fff" stroke-width="2"/><path d="m10 10 5 5" stroke="#fff" stroke-width="2"/></svg></span></div>
  <div class="tile-body blue" style="height:165px"><div class="tile-title">Big Kids Helping Little Kids !</div><div class="tile-rule"></div><div class="tile-text">Every comic sold helps a child smile. We give part of each sale to local kids.</div><div class="tile-more"><svg width="14" height="10" viewBox="0 0 14 10"><path d="M0 1h14M0 5h14M0 9h14" stroke="#fff"/></svg>READ MORE</div></div>
</article>

<section class="abs mission" role="img" aria-label="Photo of a row of smiling children lying on the grass"></section>
<div class="abs mission-text">
  <div class="mission-lead">TO SUPPORT CHILDREN'S CHARITIES WITH A PORTION OF OUR PROFITS.</div>
  <div class="mission-main">WE BELIEVE HAPPY KIDS BECOME HAPPY ADULTS !</div>
</div>
<a class="abs btn mission-btn">VIEW CHARITY</a>

<!-- products -->
<article class="abs product" style="left:138px;top:2373px">
  <div class="product-cover"><div style="background:linear-gradient(160deg,#2d6fb8,#e8c23a 60%,#d2403a)" role="img" aria-label="Comic book cover"></div></div>
  <div class="product-body orange"><div class="tile-title">Big Kids Helping Little Kids !</div><div class="tile-rule"></div><div class="tile-text">Rare issues and fresh arrivals, bagged and boarded, ready for your shelf.</div><div class="tile-more"><svg width="14" height="10" viewBox="0 0 14 10"><path d="M0 1h14M0 5h14M0 9h14" stroke="#fff"/></svg>READ MORE</div>
    <div class="product-actions"><span><svg width="13" height="13" viewBox="0 0 16 16"><circle cx="6.5" cy="6.5" r="5" fill="none" stroke="#fff" stroke-width="2"/><path d="m10 10 5 5" stroke="#fff" stroke-width="2"/></svg></span><span><svg width="16" height="10" viewBox="0 0 16 10"><path d="M1 5Q8-3 15 5Q8 13 1 5Z" fill="none" stroke="#fff" stroke-width="1.5"/><circle cx="8" cy="5" r="2" fill="#fff"/></svg></span><span style="color:#fff;font-weight:700;font-size:14px">?</span></div></div>
</article>
<article class="abs product" style="left:607px;top:2373px">
  <div class="product-cover"><div style="background:linear-gradient(160deg,#1f4f9a,#d43b35 55%,#f1c84b)" role="img" aria-label="Comic book cover"></div></div>
  <div class="product-body blue"><div class="tile-title">Big Kids Helping Little Kids !</div><div class="tile-rule"></div><div class="tile-text">Rare issues and fresh arrivals, bagged and boarded, ready for your shelf.</div><div class="tile-more"><svg width="14" height="10" viewBox="0 0 14 10"><path d="M0 1h14M0 5h14M0 9h14" stroke="#fff"/></svg>READ MORE</div></div>
</article>
<article class="abs product" style="left:138px;top:2580px">
  <div class="product-cover"><div style="background:linear-gradient(160deg,#d43b35,#2d6fb8 55%,#e8c23a)" role="img" aria-label="Comic book cover"></div></div>
  <div class="product-body yellow"><div class="tile-title">Big Kids Helping Little Kids !</div><div class="tile-rule"></div><div class="tile-text">Rare issues and fresh arrivals, bagged and boarded, ready for your shelf.</div><div class="tile-more"><svg width="14" height="10" viewBox="0 0 14 10"><path d="M0 1h14M0 5h14M0 9h14" stroke="#fff"/></svg>READ MORE</div>
    <div class="product-actions"><span><svg width="13" height="13" viewBox="0 0 16 16"><circle cx="6.5" cy="6.5" r="5" fill="none" stroke="#fff" stroke-width="2"/><path d="m10 10 5 5" stroke="#fff" stroke-width="2"/></svg></span><span><svg width="16" height="10" viewBox="0 0 16 10"><path d="M1 5Q8-3 15 5Q8 13 1 5Z" fill="none" stroke="#fff" stroke-width="1.5"/><circle cx="8" cy="5" r="2" fill="#fff"/></svg></span><span style="color:#fff;font-weight:700;font-size:14px">?</span></div></div>
</article>
<article class="abs product" style="left:607px;top:2580px">
  <div class="product-cover"><div style="background:linear-gradient(160deg,#2d6fb8,#3a86c9 50%,#e8c23a)" role="img" aria-label="Comic book cover"></div></div>
  <div class="product-body purple"><div class="tile-title">Big Kids Helping Little Kids !</div><div class="tile-rule"></div><div class="tile-text">Rare issues and fresh arrivals, bagged and boarded, ready for your shelf.</div><div class="tile-more"><svg width="14" height="10" viewBox="0 0 14 10"><path d="M0 1h14M0 5h14M0 9h14" stroke="#fff"/></svg>READ MORE</div></div>
</article>
<a class="abs btn more-btn">VIEW MORE PRODUCTS</a>

<footer class="abs footer"></footer>
<div class="abs footer-h" style="left:138px;top:2970px">CONTACT US !</div>
<div class="abs field" style="left:138px;top:3036px;width:200px">NAME</div>
<div class="abs field" style="left:365px;top:3036px;width:215px">EMAIL</div>
<div class="abs field" style="left:138px;top:3092px;width:442px;padding-bottom:36px">MESSAGE</div>
<a class="abs btn send">SEND</a>

<div class="abs footer-h" style="left:629px;top:2970px">GALLERY PHOTOS !</div>
<div class="abs gallery" role="img" aria-label="Grid of nine small photos of families and children reading">
  <div style="background:#b9a08a"></div><div style="background:#8eb1c9"></div><div style="background:#c9b29b"></div>
  <div style="background:#a7c08e"></div><div style="background:#d0b7a0"></div><div style="background:#9cb8cf"></div>
  <div style="background:#c4a68c"></div><div style="background:#b6c6a2"></div><div style="background:#a9b9c8"></div>
</div>

<div class="abs footer-h" style="left:888px;top:2970px">OTHER DETAILS !</div>
<div class="abs" style="left:888px;top:3036px">
  <div class="detail"><svg width="12" height="12" viewBox="0 0 10 10"><path d="M2 0 4 3 3 4.5Q4.5 7 6 7L7 6l3 2-1.5 2Q1 9 0 1.5Z" fill="#cfd0d2"/></svg>555-210-3389</div>
  <div class="detail"><svg width="13" height="10" viewBox="0 0 12 9"><rect x=".5" y=".5" width="11" height="8" fill="none" stroke="#cfd0d2"/><path d="M.5.5 6 5l5.5-4.5" fill="none" stroke="#cfd0d2"/></svg>martin@vantelpanels.example</div>
  <div class="detail"><svg width="10" height="13" viewBox="0 0 8 11"><path d="M4 11S0 6 0 4a4 4 0 0 1 8 0c0 2-4 7-4 7Z" fill="#cfd0d2"/></svg>PO Box 482 Larkfield Valley 17099</div>
</div>

<div class="abs bottom">
  <span>© Copyright 2015. Vantel Panels &amp; Collectibles</span>
  <span class="social"><i style="background:#3b5b99"></i><i style="background:#42a6dd"></i><i style="background:#d24b3c"></i><i style="background:#c8283c"></i></span>
</div>

</body>
</html>
```